Red heron

Retail sales of clothing related to outdoor sports, exercise, activities and socialization
Updates

please use more clothing accessories
golf beach sports running yoga pilates gym etc rather than equipment for now

please use logo designed

hello

can I get a link / page to
RED HERON MENTAL HEALTH GROUP CIC
promoting outdoor activities, exercis, outdoors and socialization to help with mental health issues
Courage strength and loyalty

use the social media image 2 wolves howling to the moon

Please

This is a non profit charity
proceeds from red heron LLC sales will be donated to this non profit company to help those in UK with mental health issues

Target Market(s)

All

Industry/Entity Type

Retail e-commerce

Coding

Coded - Design and coding required

Number of Pages Required

5+ page

Font styles to use
Other font styles liked:
• To fit with red heron logo design

Colors
0054AA
0677BA
7BADD7
CADEEF
E8F1F8

Requirements
Must have
• Ability to accept payments, link to a not for profit business to be supplied for donations of proceeds of sale, ability to link to activities
Nice to have
• Ai associated customers service, email, blog, WhatsApp, links to social media

```html
<!DOCTYPE html>
<html lang="en">
<head>
<meta charset="utf-8">
<title>Red Heron — Outdoor Clothing &amp; Social Games</title>
<link rel="stylesheet" href="https://fonts.googleapis.com/css2?family=Libre+Baskerville:wght@700&family=Roboto:wght@400;500;700&display=swap">
<style>
:root{
  --brand:#0b3c9c;
  --brand-deep:#08307f;
  --brand-mid:#0054aa;
  --sky:#c7daee;
  --mist:#e8f1f8;
  --ink:#1d1d1f;
  --muted:#6b6f76;
  --line:#e3e6ea;
  --star:#f5a623;
  --white:#ffffff;
}
*{box-sizing:border-box;margin:0;padding:0}
html,body{width:1200px;height:4942px;overflow:hidden}
body{position:relative;font-family:"Roboto",Arial,sans-serif;color:var(--ink);background:var(--white);font-size:13px}
.abs{position:absolute}
.serif{font-family:"Libre Baskerville",Georgia,serif;font-weight:700}
.btn{position:absolute;display:flex;align-items:center;justify-content:center;font-weight:700;font-size:15px;letter-spacing:.3px}
.btn-solid{background:var(--brand);color:var(--white)}
.btn-light{background:var(--white);color:var(--brand)}
.btn-outline{background:var(--white);color:var(--brand);border:1px solid var(--brand)}
.photo{position:absolute}
.section-title{position:absolute;left:0;width:1200px;text-align:center;font-size:34px;color:var(--ink)}
.rule{position:absolute;left:575px;width:50px;height:4px;background:var(--brand)}

/* top bar */
.topbar{top:0;left:0;width:1200px;height:36px;background:var(--sky);font-size:11px}
.topbar span{position:absolute;top:11px}
/* header */
.header{top:36px;left:0;width:1200px;height:79px;background:var(--white)}
.logo{position:absolute;left:112px;top:22px;display:flex;align-items:center;gap:10px;font-size:26px;color:var(--brand)}
.logo i{display:block;width:30px;height:30px;border-radius:50%;background:var(--brand)}
.nav a{position:absolute;top:29px;font-size:14px;font-weight:500;color:var(--ink);text-decoration:none}
.nav a.active{color:var(--brand)}
/* hero */
.hero{top:115px;left:0;width:1200px;height:560px;background:linear-gradient(115deg,#2f3a44 0%,#56667a 38%,#8a8b86 62%,#3b342b 100%)}
.hero h1{position:absolute;left:112px;top:170px;font-size:58px;color:var(--white);letter-spacing:1px}
.hero p{position:absolute;left:112px;top:262px;width:490px;font-size:16px;line-height:28px;color:var(--white)}
.pager{position:absolute;left:572px;top:504px;color:var(--white);font-size:14px}
/* categories */
.cat{top:692px;width:279px;height:355px;border-radius:6px;overflow:hidden}
.cat .label{position:absolute;left:12px;right:12px;bottom:14px;height:50px;background:var(--white);display:flex;align-items:center;justify-content:center;font-weight:700;font-size:17px;border-radius:3px}
.cat .label.active{background:var(--brand);color:var(--white)}
/* products */
.prod{width:232px;text-align:center}
.prod .img{height:269px}
.prod .name{margin-top:22px;font-size:19px}
.prod .price{margin-top:6px;color:var(--brand);font-weight:700;font-size:16px}
/* sale */
.sale{top:1774px;left:0;width:1200px;height:283px;background:linear-gradient(180deg,#0d3f9f,#0a3790)}
/* trending */
.tcard{top:2238px;width:231px;height:427px;border:1px solid var(--line);background:var(--white);box-shadow:0 2px 6px rgba(0,0,0,.08)}
.tcard .tag{position:absolute;left:14px;top:16px;background:#3b6fd1;color:var(--white);font-size:9px;padding:3px 5px}
.tcard .quick{position:absolute;right:14px;top:16px;font-size:11px;text-decoration:underline}
.tcard .img{position:absolute;left:14px;top:32px;width:201px;height:196px}
.tcard .cat-t{position:absolute;top:246px;width:100%;text-align:center;color:var(--muted);font-size:12px}
.tcard .name{position:absolute;top:266px;width:100%;text-align:center;font-weight:500;font-size:16px}
.tcard .pr{position:absolute;top:296px;width:100%;text-align:center;font-size:17px;font-weight:700;color:var(--brand)}
.tcard .pr s{font-size:12px;color:var(--muted);font-weight:400;margin-right:8px}
.tcard .qty{position:absolute;top:334px;left:36px;font-size:12px}
.tcard .stepper{position:absolute;top:328px;left:94px;width:114px;height:28px;border:1px solid var(--line);display:flex;justify-content:space-between;align-items:center;padding:0 12px;font-size:14px}
.tcard .add{left:8px;top:381px;width:213px;height:34px;font-size:14px}
.arrow-sq{position:absolute;width:30px;height:30px;background:var(--brand);color:var(--white);display:flex;align-items:center;justify-content:center;font-size:16px}
/* about */
.about{top:2760px;left:0;width:1200px;height:508px;background:linear-gradient(180deg,#1149b0,#0b3e9c)}
.about p{position:absolute;left:617px;width:475px;color:var(--white);font-size:13px;line-height:22px}
/* blog */
.post{top:3452px;width:307px;height:400px;border:1px solid var(--line);background:var(--white);box-shadow:0 2px 6px rgba(0,0,0,.06)}
.post .img{position:absolute;left:0;top:0;width:305px;height:215px}
.post .date{position:absolute;right:0;top:190px;background:#4d7fd0;color:var(--white);padding:6px 12px;font-size:14px;font-weight:500}
.post h3{position:absolute;left:16px;top:242px;width:270px;font-size:16px;line-height:24px;font-weight:700}
.post p{position:absolute;left:16px;top:306px;width:270px;font-size:13px;line-height:22px;color:var(--muted)}
.post .more{position:absolute;left:16px;top:362px;font-size:13px;font-weight:700;color:var(--brand)}
/* testimonials */
.clients{top:3952px;left:0;width:1200px;height:500px;background:var(--mist)}
.quote{top:4120px;width:408px;height:230px;background:var(--white);border-radius:26px;box-shadow:0 4px 14px rgba(0,0,0,.12)}
.avatar{width:116px;height:116px;border-radius:50%;background:linear-gradient(135deg,#8d99a8,#cfd6de);border:5px solid var(--white);box-shadow:0 2px 8px rgba(0,0,0,.15)}
.quote .mark{position:absolute;left:100px;top:24px;font-family:Georgia,serif;font-size:60px;line-height:1;color:var(--brand);font-weight:700}
.quote p{position:absolute;left:100px;top:78px;width:280px;font-size:13px;line-height:23px;color:var(--muted)}
.quote .who{position:absolute;left:100px;top:166px;font-weight:500;font-size:15px}
.quote .stars{position:absolute;left:100px;top:186px;color:var(--star);font-size:16px;letter-spacing:2px}
/* newsletter */
.news{top:4452px;left:0;width:1200px;height:133px;background:var(--brand-mid)}
/* footer */
.foot h4{position:absolute;top:4655px;font-size:15px;font-weight:500;letter-spacing:.3px}
.foot ul{position:absolute;top:4686px;list-style:none;font-size:11.5px;line-height:23px;color:#333}
.vline{position:absolute;top:4655px;width:1px;height:150px;background:var(--line)}
.social{display:flex;align-items:center;gap:12px;margin-bottom:6px}
.social i{display:block;width:30px;height:30px;border-radius:50%;background:var(--brand)}
.pay{position:absolute;top:4828px;width:28px;height:18px;border-radius:2px}
</style>
</head>
<body>

<!-- Top bar -->
<div class="abs topbar">
  <span style="left:112px">Free UK Postage on orders over $50</span>
  <svg class="abs" style="left:640px;top:11px" width="13" height="13" viewBox="0 0 24 24"><circle cx="10" cy="10" r="6" fill="none" stroke="#1d1d1f" stroke-width="3"/><path d="M15 15l6 6" stroke="#1d1d1f" stroke-width="3"/></svg>
  <span style="left:660px">|</span>
  <span style="left:678px;font-size:10px">Search</span>
  <svg class="abs" style="left:834px;top:12px" width="12" height="12" viewBox="0 0 24 24"><path d="M6 2l4 4-2 3c1 3 4 6 7 7l3-2 4 4-3 4C10 22 2 14 2 5z" fill="#1d1d1f"/></svg>
  <span style="left:852px">(1) 555 010 2040</span>
  <span style="left:988px">Sign In &nbsp;|&nbsp; Register</span>
</div>

<!-- Header -->
<header class="abs header">
  <div class="logo serif"><span>RED</span><i></i><span>HERON</span></div>
  <nav class="nav">
    <a class="active" style="left:460px">Home</a>
    <a style="left:532px">About Us</a>
    <a style="left:626px">Shop ▾</a>
    <a style="left:705px">Latest</a>
    <a style="left:778px">Sale</a>
    <a style="left:840px">Blog</a>
    <a style="left:902px">Contact Us</a>
    <a class="active" style="left:1018px">🛒&#xFE0E; Cart (0)</a>
  </nav>
</header>

<!-- Hero -->
<section class="abs hero" role="img" aria-label="Hikers walking along a mountain ridge above a lake">
  <h1 class="serif">RED HERON</h1>
  <p>Lorem ipsum dolor sit amet, consectetur adipiscing elit, sed incididunt ut labore et dolore magna aliqua.</p>
  <div class="btn btn-solid" style="left:112px;top:346px;width:140px;height:48px">SHOP NOW</div>
  <div class="pager">‹ &nbsp;1/3&nbsp; ›</div>
</section>

<!-- Categories -->
<div class="abs cat" style="left:18px;background:linear-gradient(160deg,#5a4a3d,#c85a2a 50%,#3a3230)" role="img" aria-label="Outdoor gear laid out flat with an orange backpack">
  <div class="label">Outdoor Gear</div></div>
<div class="abs cat" style="left:313px;background:linear-gradient(160deg,#4f6e66,#7d9a8f 50%,#8b7a5e)" role="img" aria-label="Green tent on rocky ground with camping kit">
  <div class="label">Camping Essentials</div></div>
<div class="abs cat" style="left:608px;background:linear-gradient(180deg,#4d6b2e,#8fa44d 45%,#9fd0dc)" role="img" aria-label="Friends playing a lawn toss game in a park">
  <div class="label active">Social Games</div></div>
<div class="abs cat" style="left:904px;background:linear-gradient(160deg,#6b5043,#e9e9ea 40%,#d8d8d8)" role="img" aria-label="White hooded sweatshirt">
  <div class="label">Apparel</div></div>

<!-- New arrivals -->
<h2 class="section-title serif" style="top:1130px">NEW ARRIVALS</h2>
<div class="rule" style="top:1182px"></div>
<div class="abs prod" style="left:112px;top:1240px"><div class="img" style="background:linear-gradient(180deg,#7a9bb8,#c9d3dc 50%,#5f6b55)" role="img" aria-label="Hiker with red backpack in snowy mountains"></div><div class="name serif">Product Name</div><div class="price">$25.06</div></div>
<div class="abs prod" style="left:360px;top:1240px"><div class="img" style="background:linear-gradient(160deg,#4f7d2e,#6c6f6c 55%,#4a7a2a)" role="img" aria-label="Cornhole board on grass"></div><div class="name serif">Product Name</div><div class="price">$25.06</div></div>
<div class="abs prod" style="left:608px;top:1240px"><div class="img" style="background:linear-gradient(160deg,#5d7a3b,#c89a6a 50%,#4a5e35)" role="img" aria-label="Friends playing a giant block tower game outdoors"></div><div class="name serif">Product Name</div><div class="price">$25.06</div></div>
<div class="abs prod" style="left:857px;top:1240px"><div class="img" style="background:linear-gradient(160deg,#4c6f30,#c9a45a 50%,#3e5a28)" role="img" aria-label="Children catching a flying disc in a park"></div><div class="name serif">Product Name</div><div class="price">$25.06</div></div>
<div class="btn btn-solid" style="left:532px;top:1632px;width:136px;height:44px">VIEW ALL</div>

<!-- Sale banner -->
<section class="abs sale">
  <h2 class="serif abs" style="top:52px;width:1200px;text-align:center;font-size:34px;color:var(--white)">WINTER GEAR SALE - UP TO 30% OFF</h2>
  <div class="abs" style="top:106px;left:575px;width:50px;height:4px;background:var(--white)"></div>
  <p class="abs" style="top:134px;width:1200px;text-align:center;font-size:14px;color:var(--white)">Up to 50% off 800+ top products with new permanent price reductions</p>
  <div class="btn btn-light" style="left:535px;top:184px;width:130px;height:42px;font-size:14px">SHOP NOW</div>
</section>

<!-- Trending -->
<h2 class="section-title serif" style="top:2132px">NOW TRENDING PRODUCTS</h2>
<div class="rule" style="top:2185px"></div>
<div class="abs tcard" style="left:112px">
  <div class="tag">25% off</div><div class="quick">Quick Look</div>
  <div class="img" style="background:radial-gradient(ellipse 30% 45% at 50% 52%,#d4a86e 0%,#c99a5e 60%,#f4f6f9 62%)" role="img" aria-label="Wooden block tower game"></div>
  <div class="cat-t">Fishing Shirt</div><div class="name">Product Name</div>
  <div class="pr"><s>$25.00</s>$18.75</div>
  <div class="qty">Quantity</div><div class="stepper"><span>-</span><span>1</span><span>+</span></div>
  <div class="btn btn-solid add">Add To Cart</div>
</div>
<div class="abs tcard" style="left:360px">
  <div class="tag">25% off</div><div class="quick">Quick Look</div>
  <div class="img" style="background:radial-gradient(ellipse 40% 35% at 50% 45%,#e8303a 0%,#d81f2a 70%,#f4f6f9 72%)" role="img" aria-label="Red flying disc"></div>
  <div class="cat-t">Fishing Shirt</div><div class="name">Product Name</div>
  <div class="pr"><s>$25.00</s>$18.75</div>
  <div class="qty">Quantity</div><div class="stepper"><span>-</span><span>1</span><span>+</span></div>
  <div class="btn btn-solid add">Add To Cart</div>
</div>
<div class="arrow-sq" style="left:112px;top:2454px">‹</div>
<div class="arrow-sq" style="left:556px;top:2454px">›</div>
<div class="photo" style="left:612px;top:2238px;width:476px;height:427px;border-radius:6px;background:linear-gradient(180deg,#7fa7d4,#5d8a3c 35%,#6c8a45 60%,#d8c2a0 80%)" role="img" aria-label="Two people playing a ball game on a sandy court in a park"></div>

<!-- About -->
<section class="abs about">
  <div class="abs" style="left:112px;top:30px;width:320px;height:450px;display:flex;align-items:center;justify-content:center;gap:14px">
    <i style="display:block;width:44px;height:44px;border-radius:50%;background:var(--white)"></i>
    <span class="serif" style="color:var(--white);font-size:40px">RED HERON</span>
  </div>
  <h2 class="serif abs" style="left:617px;top:95px;font-size:34px;color:var(--white)">ABOUT US</h2>
  <p style="top:182px">Lorem ipsum dolor sit amet, consectetur adipiscing elit, sed do eiusmod tempor incididunt ut labore et dolore magna aliqua. Ut enim ad minim veniam, quis nostrud exercitation nisi ut aliquip ex ea commodo consequat.</p>
  <p style="top:268px">Duis aute irure dolor in reprehenderit in voluptate velit esse cillum dolore eu fugiat nulla pariatur. Excepteur sint occaecat cupidatat non proident, sunt in culpa qui officia deserunt mollit anim id est laborum.</p>
  <div class="btn btn-outline" style="left:617px;top:366px;width:136px;height:42px;font-size:14px">LEARN MORE</div>
</section>

<!-- Blog -->
<h2 class="section-title serif" style="top:3347px">LATEST BLOG</h2>
<div class="rule" style="top:3400px"></div>
<article class="abs post" style="left:112px"><div class="img" style="background:linear-gradient(180deg,#9bbf5a,#6e4a2e 50%,#5c9a34)" role="img" aria-label="Cornhole boards on a backyard lawn"></div><div class="date">Aug 24, 2024</div><h3>Lorem ipsum dolor consectetur adipiscing elit, sed do</h3><p>Sed ut perspiciatis unde omnis iste natus beatae vitae dicta sunt explicabo.</p><div class="more">READ MORE ›</div></article>
<article class="abs post" style="left:447px"><div class="img" style="background:linear-gradient(180deg,#5f8a3a,#8bb15a 55%,#6b9a3f)" role="img" aria-label="Children playing with a flying disc on a field"></div><div class="date">Aug 24, 2024</div><h3>Lorem ipsum dolor consectetur adipiscing elit, sed do</h3><p>Sed ut perspiciatis unde omnis iste natus beatae vitae dicta sunt explicabo.</p><div class="more">READ MORE ›</div></article>
<article class="abs post" style="left:781px"><div class="img" style="background:linear-gradient(180deg,#a9c4dc,#5d8a3a 45%,#7aa24a)" role="img" aria-label="Girl playing a ladder toss game in a park"></div><div class="date">Aug 24, 2024</div><h3>Lorem ipsum dolor consectetur adipiscing elit, sed do</h3><p>Sed ut perspiciatis unde omnis iste natus beatae vitae dicta sunt explicabo.</p><div class="more">READ MORE ›</div></article>

<!-- Testimonials -->
<section class="abs clients">
  <h2 class="serif abs" style="top:62px;width:1200px;text-align:center;font-size:34px">WHAT OUR CLIENTS SAY</h2>
  <svg class="abs" style="left:40px;top:228px" width="22" height="36" viewBox="0 0 22 36"><path d="M18 2L4 18l14 16" fill="none" stroke="#8a8f96" stroke-width="4"/></svg>
  <svg class="abs" style="left:1138px;top:228px" width="22" height="36" viewBox="0 0 22 36"><path d="M4 2l14 16L4 34" fill="none" stroke="#8a8f96" stroke-width="4"/></svg>
</section>
<div class="abs quote" style="left:170px"><div class="mark">“</div><p>Lorem ipsum amet, consectetur adipiscing elit, sed do eiusmod tempor incididunt ut labore et dolore magna aliqua.</p><div class="who">Maya</div><div class="stars">★★★★★</div></div>
<div class="abs avatar" style="left:118px;top:4172px" role="img" aria-label="Customer portrait"></div>
<div class="abs quote" style="left:680px"><div class="mark">“</div><p>Lorem ipsum amet, consectetur adipiscing elit, sed do eiusmod tempor incididunt ut labore et dolore magna aliqua.</p><div class="who">Owen</div><div class="stars">★★★★★</div></div>
<div class="abs avatar" style="left:628px;top:4172px" role="img" aria-label="Customer portrait"></div>

<!-- Newsletter -->
<section class="abs news">
  <svg class="abs" style="left:0;top:0" width="620" height="133"><path d="M0 0H620L590 133H0Z" fill="#0b3c9c"/></svg>
  <svg class="abs" style="left:80px;top:32px" width="78" height="70" viewBox="0 0 78 70"><g fill="none" stroke="#fff" stroke-width="3"><path d="M4 28L39 4l35 24v38H4Z"/><path d="M4 28l35 24 35-24"/><path d="M4 66l28-22M74 66L46 44"/><path d="M16 20V12h46v8"/><path d="M24 20h30M24 28h30"/></g></svg>
  <div class="serif abs" style="left:184px;top:34px;font-size:32px;color:var(--white)">NEWSLETTER</div>
  <div class="abs" style="left:184px;top:84px;font-size:13px;color:var(--white)">Sign up to receive exclusive offers &amp; the best deals.</div>
  <div class="abs" style="left:642px;top:38px;width:390px;height:56px;background:var(--white);display:flex;align-items:center;padding-left:20px;gap:10px;font-size:13px;color:var(--muted)">
    <svg width="14" height="11" viewBox="0 0 14 11"><rect x="1" y="1" width="12" height="9" fill="none" stroke="#6b6f76"/><path d="M1 1l6 5 6-5" fill="none" stroke="#6b6f76"/></svg>Email address</div>
  <div class="abs" style="left:1032px;top:38px;width:56px;height:56px;background:#1659c4;display:flex;align-items:center;justify-content:center">
    <svg width="24" height="24" viewBox="0 0 24 24"><path d="M2 11L22 2l-6 20-5-8z" fill="#fff"/></svg></div>
</section>

<!-- Footer -->
<footer class="foot">
  <h4 style="left:116px">QUICK LINKS</h4>
  <ul style="left:116px"><li>Home</li><li>About</li><li>Products</li><li>Shop now</li><li>Sign in</li></ul>
  <div class="vline" style="left:274px"></div>
  <h4 style="left:352px">INFORMATION</h4>
  <ul style="left:352px"><li>Terms &amp; Conditions</li><li>Privacy Policy</li><li>Disclaimer</li><li>Site Map</li><li>Contact Us</li><li>Categories</li></ul>
  <div class="vline" style="left:540px"></div>
  <h4 style="left:617px">CONTACT INFO</h4>
  <ul style="left:617px;line-height:26px">
    <li><span style="color:var(--brand)">☎&#xFE0E;</span>&nbsp; (215) 555-0142</li>
    <li><span style="color:var(--brand)">☎&#xFE0E;</span>&nbsp; (215) 555-0142</li>
    <li><span style="color:var(--brand)">✉&#xFE0E;</span>&nbsp; <u>hello@redheronshop.com</u></li>
    <li style="line-height:14px;margin-top:6px;padding-left:27px;width:200px;text-indent:-27px"><span style="color:var(--brand)">⚲</span>&nbsp;&nbsp; #2868 Lorem ipsum dolor sit amet, consectetur</li>
  </ul>
  <div class="vline" style="left:878px"></div>
  <h4 style="left:956px">FOLLOW US</h4>
  <div class="abs" style="left:956px;top:4688px;font-size:11.5px">
    <div class="social"><i></i>Social feed</div>
    <div class="social"><i></i>Photo feed</div>
    <div class="social"><i></i>Work network</div>
  </div>
  <div class="pay" style="left:112px;background:#2b3f8f"></div>
  <div class="pay" style="left:146px;background:#d8dce4"></div>
  <div class="pay" style="left:180px;background:#2f7bd1"></div>
  <div class="pay" style="left:214px;background:#e7e2da"></div>
  <div class="pay" style="left:248px;background:#2563b8"></div>
  <div class="abs" style="left:0;top:4830px;width:1200px;text-align:center;font-size:10.5px">Copyrights © Red Heron LLC 2025 | Allrights Reserved</div>
  <div class="abs" style="left:886px;top:4830px;font-size:12.5px;font-weight:700">Need Help? Ask Red Heron</div>
  <div class="abs" style="left:1060px;top:4822px;width:28px;height:28px;border-radius:50%;background:var(--brand)"></div>
</footer>

</body>
</html>
```